Business Cards for Tech Company - vLumowren

We would like new modern business cards designed for our company. Attached are some examples of other business cards we like. <br/><br/>Info we need is: <br/>First Name, Last Name<br/>Address<br/>Store Phone<br/>Cell Phone<br/>Email Address<br/>Text Logo <br/>And Other Logo<br/>

Industry/Entity Type

Technology Equipment

Contact Information for Business Card

Please use these details as example:

Brent Lodd
Technology Specialist
Direct 555.617.4089
Phone 555-730-1826

brent.lodd@vlumowren.example

6120 Tallis Lane
Harlow Park, ST 00000

Font styles to use
Sans Serif
Other font styles liked:
• Anything easy to read and modern

Colors

Designer to choose colors to be used in the design.

Requirements
Must have
• Both Logos
• Signature as name
• Use the text logo and use the shark logo but do not use the full shark logo. Have it where it is zoomed in and is expanding out of the card.
Nice to have
• Keep it clean and modern
• We like blue, white, and black/grays.
Should not have
• Random icons for phone and address.

```html
<!DOCTYPE html>
<html lang="en">
<head>
<meta charset="utf-8">
<title>vLumowren Business Cards</title>
<link rel="stylesheet" href="https://fonts.googleapis.com/css2?family=Open+Sans:wght@400;600;700&display=swap">
<style>
  :root {
    --bg: #e9e7e4;
    --card: #2a2b2d;
    --emboss: #343537;
    --white: #f4f5f7;
    --blue: #3a7fd5;
    --blue-light: #35b6e8;
  }
  * { box-sizing: border-box; margin: 0; padding: 0; }
  html, body {
    width: 1200px; height: 847px; overflow: hidden;
    background: var(--bg);
    font-family: "Open Sans", Arial, sans-serif;
  }
  .stage { position: relative; width: 1200px; height: 847px; }
  .card {
    position: absolute;
    width: 520px; height: 297px;
    background: var(--card);
    border-radius: 3px;
    box-shadow: 0 6px 18px rgba(0,0,0,.25);
  }
  .card-back { left: 70px; top: 110px; }
  .card-front { left: 610px; top: 440px; }

  .back-wordmark {
    position: absolute; left: 0; right: 0; top: 118px;
    text-align: center;
    font-size: 52px; font-weight: 700; letter-spacing: -1px;
    color: var(--emboss);
  }

  .front-wordmark {
    position: absolute; left: 250px; top: 46px;
    display: flex; align-items: center; gap: 10px;
  }
  .front-wordmark .mark-square { width: 14px; height: 14px; background: var(--blue); }
  .front-wordmark .name {
    font-size: 36px; font-weight: 700; color: var(--white); letter-spacing: -0.5px;
  }

  .person { position: absolute; left: 40px; top: 140px; }
  .person-name {
    font-size: 19px; font-weight: 600; color: var(--blue); letter-spacing: .5px;
  }
  .person-title { font-size: 14px; color: var(--white); margin-top: 2px; }

  .divider {
    position: absolute; left: 222px; top: 140px;
    width: 1px; height: 58px; background: var(--blue);
  }

  .contacts { position: absolute; left: 236px; top: 140px; list-style: none; }
  .contacts li {
    display: flex; align-items: center; gap: 7px;
    font-size: 14px; color: var(--white); line-height: 20px;
  }
  .contacts svg { width: 12px; height: 12px; flex: none; }

  .address {
    position: absolute; left: 40px; top: 226px;
    font-size: 14px; color: var(--white);
  }
</style>
</head>
<body>
<main class="stage">
  <section class="card card-back">
    <div class="back-wordmark">vLumowren</div>
  </section>

  <section class="card card-front">
    <div class="front-wordmark">
      <span class="name">vLumowren</span>
      <span class="mark-square"></span>
    </div>

    <div class="person">
      <div class="person-name">BRENT LODD</div>
      <div class="person-title">Technology Specialist</div>
    </div>

    <div class="divider"></div>

    <ul class="contacts">
      <li>
        <svg viewBox="0 0 12 12" aria-hidden="true"><path fill="#35b6e8" d="M2.5 1 4.5 1 5 3.5 3.8 4.4C4.5 5.9 6 7.4 7.6 8.2L8.5 7 11 7.5 11 9.5C11 10.3 10.3 11 9.5 11 5 11 1 7 1 2.5 1 1.7 1.7 1 2.5 1Z"/></svg>
        555.617.4089
      </li>
      <li>
        <svg viewBox="0 0 12 12" aria-hidden="true"><rect x="3" y="0.5" width="6" height="11" rx="1" fill="none" stroke="#35b6e8" stroke-width="1.2"/><circle cx="6" cy="9.5" r=".7" fill="#35b6e8"/></svg>
        555-730-1826
      </li>
      <li>
        <svg viewBox="0 0 12 12" aria-hidden="true"><rect x="1" y="2.5" width="10" height="7" fill="#35b6e8"/><path d="M1 2.5 6 6.5 11 2.5" fill="none" stroke="#2a2b2d" stroke-width="1"/></svg>
        brent.lodd@vlumowren.example
      </li>
    </ul>

    <div class="address">6120 Tallis Lane, Harlow Park, ST 00000</div>
  </section>
</main>
</body>
</html>
```